I am a highly experienced private practice psychotherapist serving high end clientele in the Wall Street area of New York City. I need electronic letterhead (that can also be printed) to use for bills, receipts, and correspondences.

My clients are very high end and are used to elegance and wealth. The letterhead should contain the following information: Marissa K. Tolland, LCSW 57 Pinegate Avenue, Suite 2716 New York, NY 10392 Phone : (917) 555-3179 email: therapy@marissatollandlcsw.example website: www.marissatollandlcsw.example

Thank you for your designs. Please be advised that the letterhead will be used for bills/invoices; professional letters to other mental health professionals and doctors, as well as to attorneys. It needs to be highly professional in the same way that a law firm has professional and elegant letterhead, raher than whimsical or with spa designers. My letters end up as official documents.

```html
<!DOCTYPE html>
<html lang="en">
<head>
<meta charset="utf-8">
<title>Marissa K. Tolland, LCSW — Letterhead</title>
<link rel="stylesheet" href="https://fonts.googleapis.com/css2?family=Open+Sans:wght@400;700&display=swap">
<style>
  :root {
    --blue-light: #6ab6e8;
    --blue-mid: #0a78c2;
    --blue-deep: #0d4b9e;
    --paper: #ffffff;
    --text-on-blue: #ffffff;
  }
  * { box-sizing: border-box; margin: 0; padding: 0; }
  html, body {
    width: 933px;
    height: 1200px;
    overflow: hidden;
    background: var(--paper);
  }
  .letterhead {
    position: relative;
    width: 933px;
    height: 1200px;
    background: var(--paper);
    font-family: "Open Sans", Arial, sans-serif;
  }
  .letterhead__header {
    position: absolute;
    top: 0;
    left: 0;
    width: 933px;
    height: 150px;
  }
  .letterhead__wave { display: block; width: 100%; height: 100%; }
  .letterhead__name {
    position: absolute;
    top: 44px;
    left: 36px;
    font-size: 30px;
    font-weight: 400;
    color: var(--text-on-blue);
    letter-spacing: 0.2px;
  }
  .letterhead__footer {
    position: absolute;
    left: 0;
    bottom: 0;
    width: 933px;
    height: 54px;
    background: linear-gradient(90deg, var(--blue-light) 0%, var(--blue-mid) 55%, var(--blue-deep) 100%);
    display: flex;
    align-items: center;
    padding: 0 10px;
  }
  .contact-line {
    font-size: 10.6px;
    color: var(--text-on-blue);
    white-space: nowrap;
  }
  .contact-line__label { font-weight: 700; }
  .contact-line__item + .contact-line__item { margin-left: 4px; }
</style>
</head>
<body>
  <div class="letterhead">
    <header class="letterhead__header">
      <svg class="letterhead__wave" viewBox="0 0 933 150" preserveAspectRatio="none" aria-hidden="true">
        <defs>
          <linearGradient id="headerGradient" x1="0" y1="0" x2="1" y2="0">
            <stop offset="0" stop-color="var(--blue-light)"/>
            <stop offset="0.6" stop-color="var(--blue-mid)"/>
            <stop offset="1" stop-color="var(--blue-deep)"/>
          </linearGradient>
        </defs>
        <path d="M0,0 H933 V52 C780,50 580,68 440,96 C300,124 150,142 0,148 Z" fill="url(#headerGradient)"/>
      </svg>
      <h1 class="letterhead__name">Marissa K. Tolland, LCSW</h1>
    </header>

    <footer class="letterhead__footer">
      <p class="contact-line">
        <span class="contact-line__item"><span class="contact-line__label">Phone:</span> (917) 555-3179</span>
        <span class="contact-line__item"><span class="contact-line__label">E-mail:</span> therapy@marissatollandlcsw.example</span>
        <span class="contact-line__item"><span class="contact-line__label">Web:</span> www.marissatollandlcsw.example</span>
        <span class="contact-line__item"><span class="contact-line__label">Address:</span> 57 Pinegate Avenue, Suite 2716 New York, NY 10392</span>
      </p>
    </footer>
  </div>
</body>
</html>
```